tile distributor needs a new logo and packaging designe

"BREVALO TILE & STONE LTD'' in Canada needs great logo and a graphic design for a cardboard box package for the ceramic tiles. For inspiration you can use the logo from our sister's company, www.brevalo-example.de.
In regards to the cardboard package for the ceramic tiles it should include the BREVALO new logo on white cardboard background.
The box has to have the following info:
-Company name (with slogan "ARCHITECTURAL SOLUTIONS" or similar)
-Nominal size of the tiles (we need packages for 30cm x 60cm, 60cm x 60cm,and 30cm x 90cm) with table: nominal thickness, #pieces per box and MQ/SFT per box
-product description "RECTIFIED PORCELAIN TILE"
-made in china (not too visible, small letters)
-CE sign
-Attention text:"Before tile setting, please verify...." (see the attachment)
-Emission in indoor air sign
-and the hole on the front page (the color of the tile should be visible)
All text will be translated in 3 languages (German, English and Serbian)
I have attached some samples of the competitor"s packages and our current box for your reference.
I have increased the budget for CND$100 for my project and I hope that now it will be more atractiv for designers.
Looking forward to seeing your fresh ideas.
Reason: I have just increased the budget for this project therefore I am extending the deadline.
Hope this will help to get the great design for my company logo and packaging.

```html
<!DOCTYPE html>
<html lang="en">
<head>
<meta charset="utf-8">
<title>BREVALO Group – Rectified Porcelain Tile Box 60x60</title>
<link href="https://fonts.googleapis.com/css2?family=Archivo:wght@400;600;700;800&family=Roboto:wght@400;700&display=swap" rel="stylesheet">
<style>
  :root {
    --paper: #ffffff;
    --brand-blue: #2c5f95;
    --brand-navy: #1d426f;
    --band-light: #4b8fae;
    --slate: #6b6b6b;
    --rule: #c9c9c9;
    --tile-cream: #fdeab8;
    --white: #ffffff;
  }
  * { box-sizing: border-box; margin: 0; padding: 0; }
  html, body {
    width: 1200px; height: 1177px; overflow: hidden;
    background: var(--paper);
  }
  .box-face {
    position: relative; width: 1200px; height: 1177px;
    background: var(--paper);
    font-family: 'Archivo', Arial, sans-serif;
  }
  .brand {
    position: absolute; left: 106px; top: 120px; width: 496px; height: 50px;
    display: flex; align-items: center; gap: 16px; white-space: nowrap;
  }
  .brand-mark {
    width: 30px; height: 30px; background: var(--brand-blue); flex: none;
  }
  .brand-name {
    font-weight: 700; font-size: 44px; letter-spacing: 2px;
    color: var(--brand-blue); line-height: 1;
  }
  .brand-rule {
    position: absolute; left: 106px; top: 254px; width: 496px; height: 2px;
    background: var(--rule);
  }
  .slogan {
    position: absolute; left: 106px; top: 288px; width: 484px;
    text-align: center; color: var(--slate);
    font-weight: 700; font-size: 31px; letter-spacing: 3px; line-height: 39px;
  }
  .product {
    position: absolute; left: 830px; top: 96px; width: 340px;
    text-align: center; color: var(--brand-blue);
    font-weight: 800; font-size: 31px; letter-spacing: 2.5px; line-height: 38px;
  }
  .product p + p { margin-top: 19px; }
  .tile-window {
    position: absolute; left: 244px; top: 550px; width: 910px; height: 238px;
    background: var(--tile-cream);
  }
  .info-band {
    position: absolute; left: 0; top: 880px; width: 1200px; height: 250px;
    background: linear-gradient(90deg, var(--brand-navy) 0%, #2a5a82 55%, var(--band-light) 100%);
    border-top: 3px solid var(--band-light);
    border-bottom: 3px solid var(--band-light);
    color: var(--white);
  }
  .spec-table {
    position: absolute; left: 106px; top: 31px; width: 294px; height: 184px;
    border-collapse: collapse; table-layout: fixed;
  }
  .spec-table tr { height: 61px; }
  .spec-table td {
    border: 2px solid var(--white); text-align: center; vertical-align: middle;
  }
  .spec-table .label {
    width: 200px; font-family: 'Roboto', Arial, sans-serif;
    font-size: 13.5px; line-height: 16px;
  }
  .spec-table .value {
    font-family: 'Roboto', Arial, sans-serif;
    font-weight: 700; font-size: 19px; letter-spacing: 0.5px;
  }
  .size {
    position: absolute; right: 66px; top: 36px; text-align: center;
    font-family: 'Roboto', Arial, sans-serif;
  }
  .size-metric { font-weight: 700; font-size: 86px; line-height: 88px; letter-spacing: -1px; }
  .size-imperial { font-size: 38px; line-height: 44px; }
  .origin {
    position: absolute; right: 64px; top: 203px;
    font-family: 'Roboto', Arial, sans-serif; font-size: 13px; letter-spacing: -0.2px;
  }
  .origin .dot { margin: 0 7px; }
</style>
</head>
<body>
<main class="box-face">
  <header class="brand">
    <span class="brand-mark"></span>
    <span class="brand-name">BREVALO GROUP</span>
  </header>
  <div class="brand-rule"></div>
  <p class="slogan">ARCHITECTURAL<br>SOLUTIONS</p>

  <section class="product">
    <p>RECTIFIED<br>PORCELAIN TILE</p>
    <p>REKTIFIZIERT<br>FEINSTEINZEUG</p>
    <p>ИСПРАВЉА<br>ПОРЦЕЛАН ЦРЕП</p>
  </section>

  <div class="tile-window" role="img" aria-label="Die-cut window in the box showing the tile colour"></div>

  <section class="info-band">
    <table class="spec-table">
      <tr><td class="label">NOMINAL THICKNESS<br>NENNDICKE<br>НОМИНАЛНА ДЕБЉИНА</td><td class="value">XX</td></tr>
      <tr><td class="label">PIECES - STÜCK - КОМАДА</td><td class="value">X</td></tr>
      <tr><td class="label">MQ/SFT</td><td class="value">X,XXX</td></tr>
    </table>
    <div class="size">
      <div class="size-metric">cm.60x60</div>
      <div class="size-imperial">(23.62”x23.62”)</div>
    </div>
    <p class="origin">MADE IN CHINA<span class="dot">●</span>IN CHINA HERGESTELLT<span class="dot">●</span>МАДЕ ИН ЦХИНА</p>
  </section>
</main>
</body>
</html>
```